I am seeking someone to design a placemat for our leadership team, that includes the key concepts from our work with a leadership consultant. The place mate should incorporate all of the information from the 'Leadership Placemat' document. The document contains a range of diagrams and models that i would like modified and made consistent for this placemat.

I'm wanting the placemat to be a single side A3 page, that includes some design work to make each of the concepts have a consistent visual look.

My preference would be a design that incorporates modified versions of all of the diagrams and concepts to look either highly professional in layout, look and feel.

```html
<!DOCTYPE html>
<html lang="en">
<head>
<meta charset="utf-8">
<title>Leadership Placemat 2023</title>
<link href="https://fonts.googleapis.com/css2?family=Poppins:wght@400;500;600;700;800&display=swap" rel="stylesheet">
<style>
:root{
  --bg:#c4c4c4;
  --paper:#ffffff;
  --band:#1f7a99;
  --title:#1f7f9c;
  --title-dark:#2a4b63;
  --purpose:#0aa9b5;
  --leadership:#1f87a3;
  --feedback:#2b4f6a;
  --culture:#6f8bbd;
  --teams:#2c3a47;
  --life:#12aab5;
  --teal-box:#52b0a6;
  --expect:#6a86ba;
  --self:#2b5068;
  --ink:#333c45;
  --teal:#55b3a4;
  --red:#ee5b44;
  --orange:#fbaa4a;
  --line:#9aa3ab;
}
*{box-sizing:border-box;margin:0;padding:0}
html,body{width:1200px;height:1200px;overflow:hidden;background:var(--bg);font-family:"Poppins",sans-serif;color:var(--ink)}
.poster{position:absolute;left:0;top:176px;width:1200px;height:848px;background:var(--paper);border-top:6px solid var(--band)}
.title{position:absolute;left:0;right:0;top:32px;text-align:center;font-weight:800;font-size:66px;letter-spacing:1px;line-height:1;color:var(--title)}
.title span{color:var(--title-dark)}
.panel{position:absolute;border:1px solid #b9c0c6;background:#fff;overflow:hidden}
.panel-head{height:50px;display:flex;align-items:center;justify-content:center;color:#fff;font-weight:600;font-size:17px;letter-spacing:.3px}
.panel-body{padding:8px 12px;font-size:6px;line-height:1.35}
.purpose{left:44px;top:114px;width:223px;height:372px}
.leadership{left:267px;top:114px;width:223px;height:372px}
.feedback{left:489px;top:114px;width:223px;height:545px}
.culture{left:711px;top:114px;width:223px;height:372px}
.teams{left:934px;top:114px;width:222px;height:372px}
.purpose .panel-head{background:var(--purpose)}
.leadership .panel-head{background:var(--leadership)}
.feedback .panel-head{background:var(--feedback)}
.culture .panel-head{background:var(--culture)}
.teams .panel-head{background:var(--teams)}
.bullets{list-style:none}
.bullets li{position:relative;padding-left:8px;margin-bottom:2.5px}
.bullets li::before{content:"";position:absolute;left:0;top:2px;width:3.5px;height:3.5px;border:1px solid var(--line);border-radius:50%}
.sub{font-weight:600;color:var(--feedback);margin:5px 0 2px}
/* purpose */
.why-block{display:flex;gap:8px;align-items:center}
.why-block svg{flex:none}
.why-notes{font-size:4.6px;line-height:1.3}
.why-notes b{display:block;font-weight:600;font-size:4.6px}
.concept-title{color:var(--purpose);font-size:8px;line-height:1.1;margin:8px 0 5px}
.chevrons{list-style:none}
.chevrons li{height:11px;margin-bottom:3px;color:#fff;font-size:5px;display:flex;align-items:center;padding-left:4px;clip-path:polygon(0 0,88% 0,100% 50%,88% 100%,0 100%);width:178px}
.chevrons li:nth-child(1){background:#1f7f9c}
.chevrons li:nth-child(2){background:#2b4f6a}
.chevrons li:nth-child(3){background:#6f8bbd}
.chevrons li:nth-child(4){background:#1f87a3}
.chevrons li:nth-child(5){background:#3a4a5a}
.infinite{color:var(--purpose);font-size:8px;margin:6px 0 4px}
.book{width:130px;height:70px;margin-left:6px;background:linear-gradient(#e9eef2,#cfdbe3);border-bottom:3px solid var(--leadership)}
.plain-list{margin-top:8px;font-size:5.6px;line-height:1.45}
/* leadership */
.lead-top{display:flex;gap:4px}
.lead-top .bullets{width:105px}
.scales{flex:1;display:flex;flex-direction:column;gap:4px;font-size:5px}
.scales .art{height:58px;background:linear-gradient(#f1e3c4,#d8b96f);border-radius:3px}
.decide{color:var(--feedback);font-weight:600;font-size:6.5px;margin:8px 0 4px}
.decide-grid{display:grid;grid-template-columns:1fr 1fr;gap:4px 10px}
.dark-box{background:#3e4d60;color:#fff;font-size:5.4px;line-height:1.2;padding:4px 5px;border-radius:3px;height:28px}
.brain{height:60px;border-radius:50%;width:60px;margin:0 auto;background:radial-gradient(circle at 45% 40%,#3a8fd0,#10344f 70%)}
.icon-list{list-style:none;margin-top:8px}
.icon-list li{display:flex;align-items:center;gap:6px;margin-bottom:4.5px;font-size:5.4px}
.icon-list i{flex:none;width:10px;height:10px;border-radius:50%;background:var(--leadership)}
/* feedback */
.feedback .panel-body{font-size:5.6px;line-height:1.32}
.fb-top{display:flex;justify-content:space-between}
.tags{display:flex;flex-direction:column;align-items:flex-end;gap:3px}
.tag{background:var(--feedback);color:#fff;font-size:5px;padding:1px 5px;border-radius:6px}
.avatars{width:42px;height:22px;border-radius:4px;background:linear-gradient(90deg,#f2c9a6,#c9d5e0)}
.feedback .bullets li{margin-bottom:1.6px}
/* culture */
.culture-box{background:var(--leadership);height:92px;margin:10px 0;display:flex;align-items:center}
.culture-box .art{width:88px;height:92px;background:radial-gradient(circle at 50% 55%,#f7c948,#e9a24a 55%,#1f87a3 75%)}
.culture-box p{flex:1;text-align:center;color:#fff;font-size:9px;line-height:1.55}
.trio{display:flex;justify-content:space-between;margin-top:10px;text-align:center;font-size:5.4px;line-height:1.25}
.trio div{width:60px}
.trio svg{display:block;margin:0 auto 4px}
/* teams */
.teams .panel-body{padding:18px 16px;font-size:6.6px}
.people{display:grid;grid-template-columns:repeat(4,38px);gap:8px 8px;margin:22px 0 26px 4px}
.people span{width:38px;height:38px;border-radius:50%}
.c-teal{background:var(--teal)}.c-red{background:var(--red)}.c-orange{background:var(--orange)}
.wary{font-size:8px}
/* life balance */
.life{left:44px;top:490px;width:446px;height:305px}
.life .panel-head{background:var(--life);font-weight:400;font-size:17px;height:49px}
.life h3{text-align:center;color:var(--purpose);font-weight:400;font-size:14.5px;margin-top:6px}
.life h4{text-align:center;color:var(--feedback);font-weight:600;font-size:13.5px;line-height:1.2}
.wheel-wrap{position:absolute;left:0;top:108px;width:446px;height:190px;font-size:8.5px;font-weight:600;color:#3b4650}
.wheel-wrap svg{position:absolute;left:127px;top:0}
.wl{position:absolute;line-height:1.1}
/* self worth */
.self{left:742px;top:491px;width:414px;height:138px}
.self .panel-head{background:var(--self);justify-content:flex-start;padding-left:30px;font-weight:400;font-size:17px;height:46px}
.self p{font-size:9.3px;padding:0 29px;margin-bottom:4px}
.self p:first-of-type{margin-top:18px}
.teal-note{position:absolute;left:489px;top:664px;width:223px;height:131px;background:var(--teal-box);color:#fff;font-size:7px;line-height:1.3;padding:36px 20px 0}
.teal-note p{margin-bottom:8px}
.expect{position:absolute;left:742px;top:635px;width:414px;height:160px;background:var(--expect);color:#fff;padding:12px 22px}
.expect h5{font-weight:400;font-size:14.5px;margin-bottom:14px}
.expect p{font-size:11px;margin-bottom:11px;padding-left:2px}
.expect svg{position:absolute;right:44px;top:36px}
</style>
</head>
<body>
<main class="poster">
  <h1 class="title">LEADERSHIP PLACEMAT <span>– 2023</span></h1>

  <section class="panel purpose">
    <div class="panel-head">PURPOSE</div>
    <div class="panel-body">
      <div class="why-block">
        <svg width="72" height="72" viewBox="0 0 72 72" aria-hidden="true">
          <circle cx="36" cy="36" r="35" fill="#9fb3d6"/>
          <circle cx="36" cy="36" r="26" fill="#6f8bbd"/>
          <circle cx="36" cy="36" r="17" fill="#2b4f6a"/>
          <text x="36" y="38" font-size="5" fill="#fff" text-anchor="middle" font-family="Poppins,sans-serif">WHAT?</text>
          <text x="36" y="57" font-size="4" fill="#fff" text-anchor="middle" font-family="Poppins,sans-serif">HOW?</text>
          <text x="36" y="69" font-size="4" fill="#fff" text-anchor="middle" font-family="Poppins,sans-serif">WHY?</text>
        </svg>
        <div class="why-notes">
          <b>WHAT?</b>The outcomes we deliver for our people and community.
          <b>HOW?</b>The way we work together every single day.
          <b>WHY?</b>The cause that guides each choice we make.
        </div>
      </div>
      <p class="concept-title">Key concepts of a performance, planning and development culture:</p>
      <ul class="chevrons">
        <li>1 – Live and lead to further a just cause</li>
        <li>1 – Build trust in teams</li>
        <li>3 – Find worthy rivals</li>
        <li>4 – Display existential flexibility to make extreme strategic shifts</li>
        <li>5 – Find the courage to lead with an infinite mindset</li>
      </ul>
      <p class="infinite">The infinite game</p>
      <div class="book" role="img" aria-label="Open book illustration comparing finite and infinite games"></div>
      <div class="plain-list">
        Live and lead to further a just cause<br>
        Build trust in teams<br>
        Find worthy rivals<br>
        Display existential flexibility to make extreme strategic shifts<br>
        Find the courage to lead with an infinite mindset
      </div>
    </div>
  </section>

  <section class="panel leadership">
    <div class="panel-head">LEADERSHIP</div>
    <div class="panel-body">
      <div class="lead-top">
        <ul class="bullets">
          <li>Leading and managing</li>
          <li>Everyone needs to know when to lead and when to manage</li>
          <li>Teachers need to be the leader of learning – in and out of the classroom!</li>
          <li>When do you need to step in and manage, direct and/or take charge?</li>
        </ul>
        <div class="scales">
          <span>(include the 80% and 20% diagram)</span>
          <div class="art" role="img" aria-label="Balance scale weighing leading against managing, 80–20"></div>
        </div>
      </div>
      <p class="decide">How do we make strategic decisions?</p>
      <div class="decide-grid">
        <div class="dark-box">But, don't get analysis paralysis. Move around all phases of the diagram.</div>
        <div class="dark-box">Levels of perspective</div>
        <div class="brain" role="img" aria-label="Head silhouette with glowing brain"></div>
        <div class="brain" role="img" aria-label="Head silhouette with glowing brain"></div>
        <div class="dark-box">Perception is your reality. Understand how you and others make meaning.</div>
        <div class="dark-box">You keep your mental models if you are operating as mostly a manager.</div>
      </div>
      <ul class="icon-list">
        <li><i></i>Purpose – Why?</li>
        <li><i></i>Vision – What you want to see</li>
        <li><i></i>Systemic structures – Systems and processes</li>
        <li><i></i>Mental model – Values and beliefs</li>
        <li><i></i>Patterns of behaviour – Habit and routines – rituals and celebrations</li>
        <li><i></i>Events – Outcomes and outputs</li>
      </ul>
    </div>
  </section>

  <section class="panel feedback">
    <div class="panel-head">FEEDBACK</div>
    <div class="panel-body">
      <div class="fb-top">
        <div>Model an effective feedback culture<br>All levels of feedback
          <ul class="bullets"><li>Teams</li><li>At level</li><li>Above level</li></ul>
        </div>
        <div class="tags"><span class="tag">Above level</span><span class="tag">At level</span>
          <div class="avatars" role="img" aria-label="Two colleague avatars"></div><span class="tag">Teams</span></div>
      </div>
      <p style="margin-top:4px">What will we – Start, stop, continue develop?</p>
      <p class="sub">Deep listening</p>
      <p class="sub">Am I:</p>
      <ul class="bullets"><li>Conversing or convincing?</li><li>Waiting to speak?</li><li>Thinking what to say?</li><li>Evaluating what is being said?</li></ul>
      <p class="sub">Skilled questions to ask:</p>
      <ul class="bullets"><li>How long has this been an issue?</li><li>What action have you taken?</li><li>What is the outcome that you are looking for?</li><li>What is the best way to move this forward?</li><li>How would you like me to be involved here?</li></ul>
      <p class="sub">After deep listening, follow up questions may help:</p>
      <ul class="bullets"><li>How will you know if you have reached a point where you are pleased with the situation?; describe what is happening.</li><li>Who else do you need to consult, and what additional date do you need to gather?</li><li>What decisions can you make now and action immediately?</li><li>What do you really want?</li><li>What are all the options available to you?</li><li>What are the priorities for you?</li><li>How would XXXX describe the situation?</li><li>How do you think XXXX feels about the situation?</li><li>What do you need to do differently to move this forward?</li></ul>
      <p class="sub">After deep listening, follow up questions may help:</p>
      <ul class="bullets"><li>How will you know if you have reached a point where you are pleased with the situation?; describe what is happening.</li><li>Who else do you need to consult, and what additional date do you need to gather?</li><li>What decisions can you make now and action immediately?</li><li>What do you really want?</li><li>What are all the options available to you?</li><li>What are the priorities for you?</li><li>How would XXXX describe the situation?</li><li>How do you think XXXX feels about the situation?</li><li>What do you need to do differently to move this forward?</li></ul>
      <p class="sub">After deep listening, follow up questions may help:</p>
    </div>
  </section>

  <section class="panel culture">
    <div class="panel-head">CULTURE</div>
    <div class="panel-body">
      <ul class="bullets" style="font-size:5.8px">
        <li style="margin-bottom:9px">Culture and strategy</li>
        <li style="margin-bottom:9px">Culture doesn't eat strategy for breakfast –</li>
        <li>Culture needs to sit down with strategy for breakfast!</li>
      </ul>
      <div class="culture-box">
        <div class="art" role="img" aria-label="Cartoon chick hatching from an egg"></div>
        <p>Culture<br>+<br>strategy</p>
      </div>
      <ul class="bullets" style="font-size:5.6px">
        <li style="margin-bottom:8px">We need a culture where people can disagree without being disagreeable</li>
        <li style="margin-bottom:8px">Resisters are not bad people or enemies – enemies are people who are actively out to get you!</li>
        <li>People to work with<br>(include diagram with Get stuff done, dream big and Know how to have fun)</li>
      </ul>
      <div class="trio">
        <div><svg width="44" height="44" aria-hidden="true"><circle cx="22" cy="22" r="21" fill="none" stroke="#2b4f6a" stroke-width="1.5"/><circle cx="22" cy="22" r="10" fill="var(--teal)"/></svg>Dream Big<br>The wishbone</div>
        <div><svg width="44" height="44" aria-hidden="true"><circle cx="22" cy="22" r="21" fill="none" stroke="#2b4f6a" stroke-width="1.5"/><rect x="12" y="15" width="20" height="14" rx="2" fill="var(--teal)"/></svg>Get work done<br>The backbone</div>
        <div><svg width="44" height="44" aria-hidden="true"><circle cx="22" cy="22" r="21" fill="none" stroke="#2b4f6a" stroke-width="1.5"/><rect x="13" y="13" width="18" height="18" rx="3" fill="var(--teal)"/></svg>Know how to have fun –<br>The funny bone</div>
      </div>
    </div>
  </section>

  <section class="panel teams">
    <div class="panel-head">TEAMS</div>
    <div class="panel-body">
      <p>Supporting teams to thrive</p>
      <p style="margin-top:9px">We will work to ensure that we are seeing the multiplication effect with our teams. We'll be mindful of burnout and ensure that we are looking after our team members.</p>
      <div class="people" role="img" aria-label="Grid of sixteen team member figures in teal, red and orange">
        <span class="c-teal"></span><span class="c-red"></span><span class="c-orange"></span><span class="c-teal"></span>
        <span class="c-teal"></span><span class="c-red"></span><span class="c-orange"></span><span class="c-teal"></span>
        <span class="c-teal"></span><span class="c-red"></span><span class="c-orange"></span><span class="c-teal"></span>
        <span class="c-teal"></span><span class="c-red"></span><span class="c-orange"></span><span class="c-teal"></span>
      </div>
      <p class="wary">Be wary of agreement!</p>
    </div>
  </section>

  <section class="panel life">
    <div class="panel-head">LIFE BALANCE</div>
    <h3>How many summers do you have left?</h3>
    <h4>PERSONAL AND STRATEGIC IMPERATIVES</h4>
    <div class="wheel-wrap">
      <span class="wl" style="left:110px;top:4px">Health</span>
      <span class="wl" style="left:286px;top:4px">Career</span>
      <span class="wl" style="left:54px;top:82px">Intrapersonal</span>
      <span class="wl" style="left:308px;top:82px">Relationships</span>
      <span class="wl" style="left:104px;top:160px">Finance</span>
      <span class="wl" style="left:286px;top:154px">Physical<br>Environment</span>
      <svg width="190" height="190" viewBox="0 0 200 200" role="img" aria-label="Life balance wheel with me at the centre">
        <g stroke="#fff" stroke-width="3">
          <path d="M26.4 57.5 A85 85 0 0 1 100 15 L100 60 A40 40 0 0 0 65.4 80 Z" fill="var(--red)"/>
          <path d="M100 15 A85 85 0 0 1 173.6 57.5 L134.6 80 A40 40 0 0 0 100 60 Z" fill="var(--teal)"/>
          <path d="M173.6 57.5 A85 85 0 0 1 173.6 142.5 L134.6 120 A40 40 0 0 0 134.6 80 Z" fill="var(--orange)"/>
          <path d="M173.6 142.5 A85 85 0 0 1 100 185 L100 140 A40 40 0 0 0 134.6 120 Z" fill="var(--red)"/>
          <path d="M100 185 A85 85 0 0 1 26.4 142.5 L65.4 120 A40 40 0 0 0 100 140 Z" fill="var(--teal)"/>
          <path d="M26.4 142.5 A85 85 0 0 1 26.4 57.5 L65.4 80 A40 40 0 0 0 65.4 120 Z" fill="var(--orange)"/>
        </g>
        <circle cx="100" cy="100" r="37" fill="#2f3640" stroke="#fff" stroke-width="3"/>
        <text x="100" y="108" text-anchor="middle" font-family="Poppins,sans-serif" font-size="22" fill="#fff">ME</text>
      </svg>
    </div>
  </section>

  <div class="teal-note">
    <p>Find self-worth independent of what you do, or you will never be satisfied!</p>
    <p>Don't get caught up in the narratives of others!</p>
    <p>I don't care about what you think about me, but I still care about you</p>
  </div>

  <section class="panel self">
    <div class="panel-head">SELF-WORTH</div>
    <p>Find self-worth independent of what you do, or you will never be satisfied!</p>
    <p>Don't get caught up in the narratives of others!</p>
    <p>I don't care about what you think about me, but I still care about you</p>
  </section>

  <section class="expect">
    <h5>Two expectations that kill performances</h5>
    <p>Expectation of outcome</p>
    <p>Expectation of what people can't control</p>
    <p>Focus on the things you can control.</p>
    <svg width="86" height="90" viewBox="0 0 86 90" aria-hidden="true">
      <g fill="#fff">
        <rect x="30" y="40" width="8" height="16"/><rect x="44" y="30" width="8" height="26"/><rect x="58" y="18" width="8" height="38"/><rect x="72" y="10" width="8" height="46"/>
        <path d="M16 62 H80 A32 26 0 0 1 16 62 Z"/>
      </g>
      <path d="M28 34 L46 20 L56 26 L76 6" stroke="#fff" stroke-width="3" fill="none"/>
      <path d="M70 4 H79 V13" stroke="#fff" stroke-width="3" fill="none"/>
    </svg>
  </section>
</main>
</body>
</html>
```